Design business cards for Valturon

I am looking for a clean, crisp and professional business card design. A logo already exists with which to work, which is attached in various formats. The design needs to be print ready. A clear brief is attached - please read it carefully and ensure you can deliver what is required. Looking forward to awarding the prize to a great design and great designer!

```html
<!DOCTYPE html>
<html lang="en">
<head>
<meta charset="utf-8">
<title>Valturon Business Card</title>
<link rel="stylesheet" href="https://fonts.googleapis.com/css2?family=Lato:wght@400;700&display=swap">
<style>
  :root {
    --backdrop: #ebe8e4;
    --card: #ffffff;
    --card-edge: #d6d2cc;
    --accent: #e8572a;
    --plum: #6b2a5e;
    --ink: #3a3a3a;
    --text: #555555;
    --bar: #333333;
  }
  html, body {
    margin: 0;
    padding: 0;
    width: 1200px;
    height: 959px;
    overflow: hidden;
    background: var(--backdrop);
    font-family: "Lato", Arial, sans-serif;
  }
  .canvas {
    position: relative;
    width: 1200px;
    height: 959px;
  }
  .card {
    position: absolute;
    left: 257px;
    width: 703px;
    height: 400px;
    background: var(--card);
    border: 1px solid var(--card-edge);
    box-shadow: 0 2px 6px rgba(0,0,0,0.12);
    overflow: hidden;
  }
  .card--front { top: 51px; }
  .card--back { top: 508px; }

  .side-bar {
    position: absolute;
    left: 0;
    top: 129px;
    width: 28px;
    height: 249px;
    background: var(--bar);
  }
  .identity {
    position: absolute;
    left: 48px;
    top: 124px;
    color: var(--text);
  }
  .identity__name {
    margin: 0;
    font-size: 24px;
    font-weight: 700;
    color: var(--accent);
    line-height: 1.1;
  }
  .identity__role {
    margin: 4px 0 0;
    font-size: 18.5px;
    line-height: 1.2;
  }
  .address {
    margin: 24px 0 0;
    font-size: 16px;
    line-height: 1.3;
    font-style: normal;
  }
  .contacts {
    list-style: none;
    margin: 12px 0 0;
    padding: 0;
    font-size: 16px;
    line-height: 20px;
  }
  .contacts li {
    display: flex;
    align-items: center;
    gap: 8px;
  }
  .contacts svg { flex: none; }

  .brand {
    position: absolute;
    display: flex;
    align-items: center;
    gap: 12px;
    color: var(--plum);
    font-weight: 700;
    line-height: 1;
  }
  .brand__dot {
    border-radius: 50%;
    background: var(--accent);
  }
  .brand--front {
    right: 40px;
    top: 110px;
    font-size: 36px;
  }
  .brand--front .brand__dot { width: 32px; height: 32px; }
  .brand--back {
    right: 38px;
    top: 274px;
    font-size: 52px;
    color: var(--ink);
    font-weight: 400;
  }
  .brand--back .brand__dot { width: 52px; height: 52px; }
  .web {
    position: absolute;
    right: 38px;
    top: 346px;
    margin: 0;
    font-size: 15px;
    letter-spacing: 2px;
    color: var(--text);
  }
  .web span { color: var(--accent); }
</style>
</head>
<body>
<main class="canvas">
  <section class="card card--front">
    <div class="side-bar"></div>
    <div class="identity">
      <h1 class="identity__name">Marcus Ellery</h1>
      <p class="identity__role">BE(Hons) PhD MIEAust GAICD<br>Director, Principal Consultant</p>
      <address class="address">42 Linden Avenue, Eastbrook<br>North Victoria 3140 Australia</address>
      <ul class="contacts">
        <li>
          <svg width="12" height="12" viewBox="0 0 12 12"><path d="M3 1 L5 3.5 L4 5 Q5 7.5 7 8 L8.5 7 L11 9 L9.5 11 Q3 10.5 1 2.5 Z" fill="var(--accent)"/></svg>
          +61 (0)400 555 123
        </li>
        <li>
          <svg width="12" height="12" viewBox="0 0 12 12"><rect x="0.5" y="2" width="11" height="8" fill="none" stroke="var(--accent)"/><path d="M0.5 2 L6 6.5 L11.5 2" fill="none" stroke="var(--accent)"/></svg>
          mellery@valturon.com.au
        </li>
        <li>
          <svg width="12" height="12" viewBox="0 0 12 12"><circle cx="6" cy="6" r="5.3" fill="none" stroke="var(--accent)"/><ellipse cx="6" cy="6" rx="2.3" ry="5.3" fill="none" stroke="var(--accent)"/><path d="M0.7 6 H11.3" stroke="var(--accent)"/></svg>
          www.valturon.com.au
        </li>
        <li>
          <svg width="12" height="12" viewBox="0 0 12 12"><rect x="0.5" y="0.5" width="11" height="11" fill="var(--accent)"/></svg>
          au.netlinker.com/in/mellery
        </li>
        <li>
          <svg width="12" height="12" viewBox="0 0 12 12"><circle cx="6" cy="6" r="5.5" fill="var(--accent)"/></svg>
          marcus.ellery40
        </li>
      </ul>
    </div>
    <div class="brand brand--front">
      <span class="brand__dot"></span>
      <span class="brand__name">Valturon</span>
    </div>
  </section>

  <section class="card card--back">
    <div class="brand brand--back">
      <span class="brand__dot"></span>
      <span class="brand__name">Valturon</span>
    </div>
    <p class="web">www.<span>valturon</span>.com.au</p>
  </section>
</main>
</body>
</html>
```